Tallow Creek Biotics - Business Card Design

Business Card Brief;
We require a design for a business card template for our business “Tallow Creek Biotics”.
We are a firm that manufacture positive microbial formulations to enhance agricultural legume crops such as lucence, soy beans and faba beans. We also manufacture microbial formulations that aid in composting of waste organic waste to use as a natural fertilizer.
We are seeking a business card design that portrays a clean, professional organisation dedicated to enhancing nature and sustainable farming techniques.
Our website is www.soilvantage.com.au
Here is a link to a drawing of a soybean plant. One of our main products is used to help grow these. I offer it an an example of the type of graphic that might be used on the card, but will leave you to create your own design; https://pixelvaultimages.com/482915066/stock-illustration-soybean-plant-on-a-white.html
Two cards are required;
--------------------------------------------------------------------
Card #1
Cody R Whitfield
Executive Chairman
Mobile: 0471 583204
Email: cody@soilvantage.com.au
---------------------------------------------------------------------------
Card #2
Lachlan P Doyce
Chief Financial & Operating Officer
Mobile: 0456 792418
Email lachlan@soilvantage.com.au

Many thanks
Lachlan Doyce

Industry/Entity Type

Agriculture

Colors

Designer to choose colors to be used in the design.

Requirements
Must have
• An elegant design that demonstrates our commitment to enhancing nature.

```html
<!DOCTYPE html>
<html lang="en">
<head>
<meta charset="utf-8">
<title>Tallow Creek Biotics – Business Cards</title>
<link rel="stylesheet" href="https://fonts.googleapis.com/css2?family=Fira+Sans:wght@300;400;700&display=swap">
<style>
  :root {
    --backdrop: #ebebeb;
    --card: #ffffff;
    --ink: #1b1b1b;
    --logo-grey: #4a4a4a;
    --mark-grey: #8c8c8c;
    --tan: #9a8064;
    --rule: #b9b9b9;
    --leaf-light: #b9e07f;
    --leaf-deep: #6fb83a;
  }
  * { box-sizing: border-box; margin: 0; padding: 0; }
  html, body {
    width: 1200px; height: 1190px; overflow: hidden;
    background: var(--backdrop);
    font-family: "Fira Sans", Arial, sans-serif;
  }
  .sheet {
    position: relative; width: 1200px; height: 1190px;
    display: flex; flex-direction: column; align-items: center; justify-content: center; gap: 70px;
  }
  .card {
    position: relative; width: 860px; height: 480px;
    background: var(--card);
    box-shadow: 0 2px 6px rgba(0,0,0,.08);
  }
  .plant-art {
    position: absolute; right: 70px; top: 40px; width: 270px; height: 250px;
    border-radius: 40% 50% 45% 55%;
    background: radial-gradient(ellipse at 45% 45%, var(--leaf-light) 0%, var(--leaf-deep) 55%, rgba(111,184,58,0) 72%);
    opacity: .75;
  }
  .brand {
    position: absolute; left: 70px; top: 190px;
    display: flex; align-items: center; gap: 16px;
  }
  .brand-dot { width: 34px; height: 34px; border-radius: 50%; background: var(--mark-grey); }
  .brand-name {
    font-weight: 300; font-size: 40px; line-height: 1; color: var(--logo-grey); letter-spacing: -0.5px;
  }
  .person { position: absolute; left: 232px; top: 270px; }
  .person-name { font-weight: 700; font-size: 26px; color: var(--ink); }
  .person-role { font-weight: 300; font-size: 19px; color: var(--tan); margin-top: 2px; }
  .divider { position: absolute; left: 232px; top: 352px; width: 22px; height: 1px; background: var(--rule); }
  .contact { position: absolute; left: 232px; top: 372px; list-style: none; }
  .contact li {
    display: flex; align-items: center; gap: 12px;
    font-size: 19px; color: var(--ink); line-height: 28px;
  }
  .contact svg { width: 16px; height: 16px; fill: var(--tan); }
</style>
</head>
<body>
<main class="sheet">

  <article class="card">
    <div class="plant-art" role="img" aria-label="Botanical illustration of a soybean plant with leaves, pods and roots"></div>
    <div class="brand"><span class="brand-dot"></span><span class="brand-name">Tallow Creek Biotics</span></div>
    <div class="person">
      <h2 class="person-name">Lachlan P Doyce</h2>
      <p class="person-role">Chief Financial &amp; Operating Officer</p>
    </div>
    <div class="divider"></div>
    <ul class="contact">
      <li><svg viewBox="0 0 16 16"><path d="M4 1l3 3-2 2c1 2 3 4 5 5l2-2 3 3-2 3C7 14 2 9 1 3z"/></svg>0456 792418</li>
      <li><svg viewBox="0 0 16 16"><path d="M1 3h14v10H1z M1 3l7 6 7-6" /></svg>lachlan@soilvantage.com.au</li>
    </ul>
  </article>

  <article class="card">
    <div class="plant-art" role="img" aria-label="Botanical illustration of a soybean plant with leaves, pods and roots"></div>
    <div class="brand"><span class="brand-dot"></span><span class="brand-name">Tallow Creek Biotics</span></div>
    <div class="person">
      <h2 class="person-name">Cody R Whitfield</h2>
      <p class="person-role">Executive Chairman</p>
    </div>
    <div class="divider"></div>
    <ul class="contact">
      <li><svg viewBox="0 0 16 16"><path d="M4 1l3 3-2 2c1 2 3 4 5 5l2-2 3 3-2 3C7 14 2 9 1 3z"/></svg>0471 583204</li>
      <li><svg viewBox="0 0 16 16"><path d="M1 3h14v10H1z M1 3l7 6 7-6" /></svg>cody@soilvantage.com.au</li>
    </ul>
  </article>

</main>
</body>
</html>
```